Trifold pamphlet for accommodation, cafe and tour business

I require a design that really stands out!
Light and bright but not garish.

See the pamphlet I have created.
This is the LAYOUT, LOGO, PHOTOS AND COPY I must have!

I require, back ground colours, images and designs to sit behind and around photos and copy.
Copy to be laid out correctly, photos laid out correctly, headings laid out correctly .
The pamphlet must flow and be captivating and want people to come visit!

I will need to provide you with high resolution photos.
Finally, I want the map provided to have our business located on it plus 2 other names.

Words that describe the business are:
Professional
Eco
Green.
Rainforest.
Birds.
Wildlife.
Adventure
Nature
Family owned and run
Family friendly.
Relaxing and beautiful.

Please check out our websites
www.tallowbrook.com.au
www.ridgeleyjourneys.com
www.facebook.com/tallowbrook
www.facebook.com/tallowbrookcafe
www.facebook.com/ridgeleyjourneys.com

I will need to provide high resolution photos.
Finally, I want the map provided to have our business located on it plus 2 other names

Thank you
Dale
dale@tallowbrook.com.au

Target Market(s)

Travellers, birdwatchers, adventurers, nature enthusiasts, family, friendly

Industry/Entity Type

Tourism

Font styles to use
Sans Serif

Colors
9bcb3c
add136
85cae6
ec1f27
fbed24

Requirements
Must have
• I require a design that really stands out!

```html
<!DOCTYPE html>
<html lang="en">
<head>
<meta charset="utf-8">
<title>Tallowbrook Trifold Pamphlet</title>
<link rel="stylesheet" href="https://fonts.googleapis.com/css2?family=Montserrat:wght@400;500;600;700;800&display=swap">
<style>
:root{
  --green:#84b843;
  --green-dark:#78aa3a;
  --red:#e52a2a;
  --white:#ffffff;
  --ink:#333333;
  --stage:#ededed;
  --sky:#1ea3e0;
  --land:#b9d84a;
}
*{box-sizing:border-box;margin:0;padding:0}
html,body{width:800px;height:1200px;overflow:hidden}
body{background:var(--stage);font-family:"Montserrat",Arial,sans-serif;color:var(--ink);position:relative}
.sheet{position:absolute;left:40px;width:720px;height:508px;display:flex;box-shadow:0 6px 18px rgba(0,0,0,.18)}
.sheet--outside{top:46px}
.sheet--inside{top:636px}
.panel{width:240px;height:100%;padding:18px 20px;position:relative}
.panel--green{background:var(--green);color:var(--white)}
.panel--white{background:var(--white)}
.heading{font-weight:600;font-size:12px;letter-spacing:.4px;text-transform:uppercase;line-height:1.2}
.panel--white .heading{color:var(--green)}
.subheading{font-weight:700;font-size:9.5px;color:var(--red);text-transform:uppercase;margin-top:8px;letter-spacing:.2px}
.subheading--line{text-decoration:underline}
.copy{font-size:7.6px;line-height:1.35;margin-top:4px}
.copy--justify{text-align:justify}
.copy--small{font-size:6.6px}
.panel--green .copy{color:#f5faef}
.photo{display:block;border:3px solid var(--white);box-shadow:0 2px 5px rgba(0,0,0,.3);position:relative}
.photo-label{position:absolute;left:0;right:0;bottom:0;background:rgba(255,255,255,.75);text-align:center;font-weight:700;font-size:12px;color:#222;padding:1px 0;letter-spacing:.5px}
.map{border:3px solid var(--white);box-shadow:0 2px 5px rgba(0,0,0,.3);background:linear-gradient(135deg,var(--sky) 0%,var(--sky) 30%,var(--land) 45%,var(--land) 70%,var(--sky) 85%)}
.rule{border-top:1.5px solid #444;margin-top:9px}
.stay-title{font-weight:600;font-size:10px;color:var(--green);text-align:center;margin-top:18px;letter-spacing:.4px}
.contact{display:flex;align-items:center;margin-top:10px}
.contact-brand{width:60px;text-align:center;font-size:6px;font-weight:700;color:var(--green);letter-spacing:.4px}
.brand-dot{width:22px;height:22px;border-radius:50%;background:#222;margin:0 auto 3px}
.contact-list{border-left:1px solid #444;padding-left:8px;list-style:none}
.contact-list li{display:flex;align-items:center;font-size:7.6px;margin:3px 0}
.contact-list li.strong{font-weight:700}
.contact-list svg{margin-right:5px;flex:none}
.cover-top{position:absolute;top:0;left:0;right:0;height:117px;background:var(--white);display:flex;flex-direction:column;align-items:center;justify-content:center}
.logo-mark{width:44px;height:44px;border-radius:50%;background:#222}
.logo-name{font-weight:600;font-size:11px;color:var(--green);letter-spacing:2.5px;margin-top:8px}
.logo-tag{font-size:4.5px;font-weight:700;letter-spacing:.6px;color:#333;margin-top:2px}
.cover-photo{position:absolute;top:117px;left:0;right:0;height:280px;background:linear-gradient(180deg,#9ec0d6 0%,#8a7560 40%,#6e5a45 70%,#8aa26a 100%)}
.cover-band{position:absolute;left:0;right:0;bottom:0;height:111px;background:var(--green);text-align:center;padding-top:24px}
.cover-band::before{content:"";position:absolute;top:-9px;left:50%;margin-left:-10px;border-left:10px solid transparent;border-right:10px solid transparent;border-bottom:10px solid var(--green)}
.cover-title{font-weight:700;font-size:16.5px;color:var(--red);letter-spacing:.6px;line-height:1}
.cover-sub{font-weight:800;font-size:21px;color:var(--white);letter-spacing:.6px;line-height:1.1;border-bottom:1.5px solid var(--white);display:inline-block;padding-bottom:2px}
.cover-url{font-weight:600;font-size:8px;color:var(--white);letter-spacing:1.3px;margin-top:11px}
.ticks{list-style:none;margin-top:8px}
.ticks li{position:relative;padding-left:10px;font-size:6.8px;line-height:1.3;margin-bottom:5px;color:#f5faef}
.ticks svg{position:absolute;left:0;top:1px}
.ticks b{color:var(--red);font-weight:600}
</style>
</head>
<body>

<section class="sheet sheet--outside">
  <div class="panel panel--green">
    <h2 class="heading">Ridgeley Journeys</h2>
    <h3 class="subheading subheading--line">Dirt Bike Tours</h3>
    <p class="copy">Experience a thrilling guided dirt bike tour on exclusive trails, the famous Frenchman's track or 3 day ride to the Tip!</p>
    <div class="photo" role="img" aria-label="Riders on dirt bikes on a grassy trail" style="height:137px;margin-top:12px;background:linear-gradient(160deg,#7fb0d8 0%,#3c5a7a 45%,#c9b23a 75%,#a0913a 100%)"></div>
    <h3 class="subheading" style="margin-top:26px">Fishing Charters / Sightseeing</h3>
    <p class="copy copy--justify">Fish unspoilt and secluded reef, estuaries and rivers to catch Mackerel, GT's,Trout, Barra, Jacks. Or come snorkelling, sightsee-ing and beach combing!</p>
    <div class="photo" role="img" aria-label="Angler on a boat holding a large fish" style="height:137px;margin-top:14px;background:linear-gradient(180deg,#a9cbe0 0%,#6f9bb5 45%,#b9b4a6 75%,#e0c12a 100%)"></div>
  </div>

  <div class="panel panel--white">
    <h2 class="heading">Getting Here</h2>
    <h3 class="subheading">By Road</h3>
    <p class="copy copy--small">Iron Range is 100km's off the Peninsula Development Road (PDR), 800kms north of Cairns. An incredibly beautiful and isolated area which can be reached, by road, during the dry season only.</p>
    <div class="map" role="img" aria-label="Map of the peninsula showing roads, national parks and the business location" style="height:246px;margin-top:12px"></div>
    <h3 class="subheading" style="margin-top:18px">By Air</h3>
    <p class="copy">Skylark Air fly into Lockhart River from Cairns Monday to Friday. <b>PH -1300 SKYLARK</b></p>
    <div class="rule"></div>
    <p class="stay-title">WE WOULD LOVE YOU TO STAY</p>
    <div class="contact">
      <div class="contact-brand"><div class="brand-dot"></div>TALLOWBROOK</div>
      <ul class="contact-list">
        <li class="strong"><svg width="8" height="8" viewBox="0 0 8 8"><circle cx="4" cy="4" r="4" fill="#e52a2a"/><path d="M2.6 2.2l.8-.2.5 1-.5.4a3 3 0 0 0 1.2 1.2l.4-.5 1 .5-.2.8C4.3 5.5 2.5 3.7 2.6 2.2z" fill="#fff"/></svg>07-4000-512</li>
        <li><svg width="8" height="8" viewBox="0 0 8 8"><circle cx="4" cy="4" r="4" fill="#e52a2a"/><rect x="2" y="2.7" width="4" height="2.8" fill="#fff"/><path d="M2 2.7l2 1.5 2-1.5" stroke="#e52a2a" stroke-width=".5" fill="none"/></svg>hello@tallowbrook.com.au</li>
        <li><svg width="8" height="8" viewBox="0 0 8 8"><circle cx="4" cy="4" r="4" fill="#e52a2a"/><circle cx="4" cy="4" r="2" fill="none" stroke="#fff" stroke-width=".6"/><path d="M2 4h4M4 2v4" stroke="#fff" stroke-width=".5"/></svg>www.tallowbrook.com.au</li>
      </ul>
    </div>
  </div>

  <div class="panel" style="padding:0;background:var(--white)">
    <div class="cover-top">
      <div class="logo-mark"></div>
      <div class="logo-name">TALLOWBROOK</div>
      <div class="logo-tag">RAINFOREST CAFE TOURS</div>
    </div>
    <div class="cover-photo" role="img" aria-label="Black palm cockatoo perched in a hollow tree trunk"></div>
    <div class="cover-band">
      <div class="cover-title">ACCOMMODATION</div>
      <div class="cover-sub">CAFE &amp; TOURS</div>
      <div class="cover-url">www.tallowbrook.com.au</div>
    </div>
  </div>
</section>

<section class="sheet sheet--inside">
  <div class="panel panel--green">
    <h2 class="heading">The Tallowbrook</h2>
    <p class="copy">We are a friendly and family run accommodation, cafe and tour business. Sitting on 250 acres of rainforest bordered by the incredible Iron Range National Park</p>
    <p class="copy" style="margin-top:10px">The Tallowbrook has Ensuite rooms, family rooms, single rooms, and private VIP accomodation. Our beach house at Portland Roads is also available.</p>
    <p class="copy" style="margin-top:10px">All have air conditioning and verandahs surrounded by beautiful gardens and scenery.</p>
    <p class="copy" style="margin-top:10px">We also have a Cafe, Guest kitchen, free WIFI, BBQ area, fire pit, plenty of parking, walking tracks and plenty of info on how to get to the best spots.</p>
    <h2 class="heading" style="margin-top:20px">The Area</h2>
    <p class="copy copy--justify">Come visit <b>Kutini Payamu (Iron range) N.P</b> World renowned for incredible rainforest, famous birdwatching, wildlife and rich in biodiversity.</p>
    <ul class="ticks">
      <li><svg width="6" height="6" viewBox="0 0 6 6"><circle cx="3" cy="3" r="2.7" fill="none" stroke="#fff" stroke-width=".6"/><path d="M1.6 3l1 1 1.8-2" stroke="#fff" stroke-width=".7" fill="none"/></svg><b>Great Barrier Reef</b> - it speaks for itself!</li>
      <li><svg width="6" height="6" viewBox="0 0 6 6"><circle cx="3" cy="3" r="2.7" fill="none" stroke="#fff" stroke-width=".6"/><path d="M1.6 3l1 1 1.8-2" stroke="#fff" stroke-width=".7" fill="none"/></svg><b>Portland Roads</b> - a tiny but beautiful and historical beach community</li>
      <li><svg width="6" height="6" viewBox="0 0 6 6"><circle cx="3" cy="3" r="2.7" fill="none" stroke="#fff" stroke-width=".6"/><path d="M1.6 3l1 1 1.8-2" stroke="#fff" stroke-width=".7" fill="none"/></svg><b>Chili beach N.P</b> - white sandy beach covered in palm trees over looking the Coral Sea. As good as it gets!</li>
      <li><svg width="6" height="6" viewBox="0 0 6 6"><circle cx="3" cy="3" r="2.7" fill="none" stroke="#fff" stroke-width=".6"/><path d="M1.6 3l1 1 1.8-2" stroke="#fff" stroke-width=".7" fill="none"/></svg><b>Riverbend Arts Centre</b> - World famous for our local indigenous artists.</li>
      <li><svg width="6" height="6" viewBox="0 0 6 6"><circle cx="3" cy="3" r="2.7" fill="none" stroke="#fff" stroke-width=".6"/><path d="M1.6 3l1 1 1.8-2" stroke="#fff" stroke-width=".7" fill="none"/></svg><b>Lockhart River Aboriginal Community</b> - Friendly and helpful indigenous community with General store, Health Care clinic, police station, Post office, bank ATM, mechanical workshop, fuel, Airport.</li>
    </ul>
  </div>

  <div class="panel panel--white">
    <h2 class="heading">Tallowbrook Rooms</h2>
    <div class="photo" role="img" aria-label="Bright ensuite bedroom with white walls" style="height:112px;margin-top:18px;background:linear-gradient(160deg,#d9d2c6 0%,#f2f0ec 50%,#c9c2b5 100%)"><span class="photo-label">ENSUITED</span></div>
    <div class="photo" role="img" aria-label="Single room with bed and window" style="height:112px;margin-top:28px;background:linear-gradient(160deg,#efe6d6 0%,#e2d2b8 50%,#f4f1ea 100%)"><span class="photo-label">SINGLE ROOM</span></div>
    <h2 class="heading" style="margin-top:30px">Our Beach House -<br>Portland Roads</h2>
    <div class="photo" role="img" aria-label="View over tropical trees to a turquoise sea" style="height:112px;margin-top:14px;background:linear-gradient(180deg,#3aa7d6 0%,#2fc0c8 45%,#4d8a3a 75%,#2f6a2a 100%)"></div>
  </div>

  <div class="panel panel--white">
    <h2 class="heading">Iron Range VIP<br>Accommodation</h2>
    <p class="copy copy--justify">Stay in our newly built 2 bedroom houses that are private, modern and have panoramic views over the rainforest and out towards the Iron Range.</p>
    <div class="photo" role="img" aria-label="Modern open plan kitchen and living area" style="height:148px;margin-top:20px;background:linear-gradient(180deg,#eeeeee 0%,#d7d7d7 55%,#6e6e6e 100%)"></div>
    <h2 class="heading" style="margin-top:28px">Tallowbrook Cafe</h2>
    <p class="copy">Enjoy a good barista coffee, delicious home made pizzas, burgers, cakes and snacks!</p>
    <div class="photo" role="img" aria-label="Burger, coffee and slice of red velvet cake" style="height:148px;margin-top:14px;background:linear-gradient(135deg,#d9a65c 0%,#f2f2f2 45%,#8b5a3a 75%,#b03a3a 100%)"></div>
  </div>
</section>

</body>
</html>
```